Performance and Functional Training for Life
Project: Business Card & Letterhead
Business Card & Letterhead
Bright & Fun-filled
Dale Varnek
Strength & Conditioning Coach
42 Millbrook Lane Harwick, MA 02740
dale@strideformlab.com
www.strideformlab.com
Whether competing on the field of play or in the game of life Stride Form Lab is your proven partner for: Performance Enhancement Injury Reduction & Rehabilitation Weight Management & Nutritional Strategies General Fitness Consulting to Companies and Schools Team Training

```html
<!DOCTYPE html>
<html lang="en">
<head>
<meta charset="UTF-8">
<title>Stride Form Lab — Business Cards</title>
<link rel="stylesheet" href="https://fonts.googleapis.com/css2?family=Questrial&display=swap">
<style>
  :root {
    --backdrop: #e4e4e4;
    --card-black: #0c0c0e;
    --card-edge: #1d1d21;
    --brand-blue: #2fa3dc;
    --text-white: #f2f2f2;
    --text-soft: #d6d6d6;
  }
  * { margin: 0; padding: 0; box-sizing: border-box; }
  html, body {
    width: 1200px; height: 901px; overflow: hidden;
    background: var(--backdrop);
    font-family: "Questrial", "Century Gothic", sans-serif;
  }
  .canvas { position: relative; width: 1200px; height: 901px; }

  .card {
    position: absolute;
    width: 560px; height: 320px;
    background: linear-gradient(150deg, var(--card-edge) 0%, var(--card-black) 45%, var(--card-black) 100%);
    border-radius: 4px;
  }

  /* Back of card */
  .card-back { left: 60px; top: 110px; text-align: center; color: var(--text-white); }
  .card-back .brand-name {
    margin-top: 44px;
    font-size: 20px; color: var(--brand-blue);
  }
  .card-back .intro {
    margin: 26px auto 0; width: 380px;
    font-size: 13px; line-height: 1.35; color: var(--text-white);
  }
  .service-list { list-style: none; margin-top: 14px; }
  .service-list li { font-size: 13px; line-height: 1.4; color: var(--brand-blue); }

  /* Front of card */
  .card-front { left: 580px; top: 470px; color: var(--text-white); }
  .identity { position: absolute; left: 32px; top: 128px; width: 280px; }
  .identity .brand-name { font-size: 28px; color: var(--text-white); letter-spacing: 0.2px; white-space: nowrap; }
  .identity .tagline { margin-top: 4px; font-size: 12px; color: var(--brand-blue); white-space: nowrap; }

  .contact { position: absolute; left: 330px; top: 66px; width: 210px; }
  .contact .person { font-size: 15px; color: var(--brand-blue); }
  .contact .role { font-size: 12px; color: var(--text-soft); margin-top: 2px; }
  .contact .address { font-size: 12px; color: var(--text-soft); margin-top: 18px; line-height: 1.4; }
  .contact-lines { list-style: none; margin-top: 22px; }
  .contact-lines li {
    display: flex; align-items: center; gap: 8px;
    font-size: 12px; color: var(--text-soft); line-height: 1.7; white-space: nowrap;
  }
  .contact-lines svg { width: 12px; height: 12px; flex: none; }
</style>
</head>
<body>
<main class="canvas">

  <section class="card card-back" aria-label="Card back">
    <div class="brand-name">Stride Form Lab</div>
    <p class="intro">Whether competing on the field of play or in the game of life Stride Form Lab is your proven partner for:</p>
    <ul class="service-list">
      <li>Performance Enhancement</li>
      <li>Injury Reduction &amp; Rehabilitation</li>
      <li>Weight Management &amp; Nutritional Strategies</li>
      <li>General Fitness</li>
      <li>Consulting to Companies and Schools</li>
      <li>Team Training</li>
    </ul>
  </section>

  <section class="card card-front" aria-label="Card front">
    <div class="identity">
      <div class="brand-name">Stride Form Lab</div>
      <div class="tagline">Performance and Functional Training for Life</div>
    </div>

    <div class="contact">
      <div class="person">Dale Varnek</div>
      <div class="role">Strength &amp; Conditioning Coach</div>
      <div class="address">42 Millbrook Lane<br>Harwick, MA 02740</div>
      <ul class="contact-lines">
        <li>
          <svg viewBox="0 0 12 12" aria-hidden="true"><path d="M3 1 L5 3.5 L4 5 Q5 7 7 8 L8.5 7 L11 9 L10 11 Q5 11 1 6 Q1 3 3 1 Z" fill="#2fa3dc"/></svg>
          781-555-0142
        </li>
        <li>
          <svg viewBox="0 0 12 12" aria-hidden="true"><rect x="1" y="2.5" width="10" height="7" rx="1" fill="none" stroke="#2fa3dc" stroke-width="1.2"/><path d="M1.5 3 L6 6.5 L10.5 3" fill="none" stroke="#2fa3dc" stroke-width="1.2"/></svg>
          dale@strideformlab.com
        </li>
        <li>
          <svg viewBox="0 0 12 12" aria-hidden="true"><circle cx="6" cy="6" r="4.8" fill="none" stroke="#2fa3dc" stroke-width="1.2"/><ellipse cx="6" cy="6" rx="2" ry="4.8" fill="none" stroke="#2fa3dc" stroke-width="1"/><line x1="1.2" y1="6" x2="10.8" y2="6" stroke="#2fa3dc" stroke-width="1"/></svg>
          www.strideformlab.com
        </li>
      </ul>
    </div>
  </section>

</main>
</body>
</html>
```